Pre-Paid Card for Teens needs a design

We are a Fintech company called Zorvella. We will sell prepaid cards for families and teens. Now we need a prepaid card design. Prepaid card should have a plexicard logo, company logo, 16 card number, expire date. Our webpage is http://www.zorvella-example.com
Target Market(s)
Teenages between 8 - 18 years old
Industry/Entity Type
It Company
Requirements
Must have
- The prepaid card must include zorvella logo, plexicard debit card logo (I already attached a sample card), 16 digit card number and expire date.
Nice to have
- It should be fun and prestigious for young people.
Should not have
- We don't want that the card has a lots of color

```html
<!DOCTYPE html>
<html lang="en">
<head>
<meta charset="utf-8">
<title>Zorvella Prepaid Card</title>
<link rel="stylesheet" href="https://fonts.googleapis.com/css2?family=Fredoka:wght@600&family=Share+Tech+Mono&family=Roboto:wght@500;700&display=swap">
<style>
  :root {
    --page-bg: #e8e5e2;
    --card-black: #050507;
    --purple-deep: #250c4c;
    --purple: #65329a;
    --yellow: #f9bd1c;
    --orange: #ee7c22;
    --white: #ffffff;
    --silver: #b9bcc2;
  }
  html, body {
    margin: 0;
    width: 1200px;
    height: 1200px;
    overflow: hidden;
    background: var(--page-bg);
  }
  .card {
    position: absolute;
    left: 121px;
    top: 299px;
    width: 958px;
    height: 602px;
    border-radius: 30px;
    overflow: hidden;
    background: var(--card-black);
  }
  .card-art {
    position: absolute;
    inset: 0;
  }
  .brand {
    position: absolute;
    left: 48px;
    top: 50px;
    display: flex;
    align-items: center;
    gap: 22px;
  }
  .brand-dot {
    width: 84px;
    height: 84px;
    border-radius: 50%;
    background: var(--yellow);
  }
  .brand-name {
    font-family: "Fredoka", sans-serif;
    font-weight: 600;
    font-size: 54px;
    color: var(--yellow);
    letter-spacing: 1px;
    line-height: 1;
  }
  .card-number {
    position: absolute;
    left: 68px;
    top: 332px;
    font-family: "Share Tech Mono", monospace;
    font-size: 44px;
    color: var(--white);
    letter-spacing: 6px;
    word-spacing: 14px;
    margin: 0;
  }
  .bin {
    position: absolute;
    left: 70px;
    top: 400px;
    font-family: "Roboto", sans-serif;
    font-weight: 700;
    font-size: 18px;
    color: var(--white);
    letter-spacing: 1px;
  }
  .valid-label {
    position: absolute;
    left: 476px;
    top: 401px;
    font-family: "Roboto", sans-serif;
    font-weight: 500;
    font-size: 15px;
    line-height: 18px;
    color: var(--white);
  }
  .valid-date {
    position: absolute;
    left: 560px;
    top: 404px;
    font-family: "Share Tech Mono", monospace;
    font-size: 34px;
    color: var(--white);
    letter-spacing: 5px;
  }
  .features {
    position: absolute;
    left: 69px;
    top: 479px;
    display: flex;
    gap: 7px;
  }
  .feature {
    width: 79px;
    height: 79px;
    border-radius: 50%;
    background: var(--orange);
    display: flex;
    align-items: center;
    justify-content: center;
  }
  .feature + .feature { margin-left: 1px; }
  .feature svg { width: 40px; height: 40px; }
  .network-badge {
    position: absolute;
    left: 749px;
    top: 328px;
    width: 172px;
    height: 226px;
    border: 2px solid var(--white);
    border-radius: 42px;
    box-sizing: border-box;
    display: flex;
    flex-direction: column;
    align-items: center;
    justify-content: space-around;
    padding: 14px 0;
  }
  .hologram {
    width: 144px;
    height: 94px;
    border-radius: 34px;
    background: linear-gradient(135deg, #8d9097, var(--silver) 45%, #6f737b);
  }
  .network-name {
    font-family: "Roboto", sans-serif;
    font-weight: 700;
    font-size: 30px;
    color: var(--white);
    line-height: 1;
  }
</style>
</head>
<body>
<div class="card">
  <svg class="card-art" viewBox="0 0 958 602" aria-hidden="true">
    <path class="swoosh-deep" fill="var(--purple-deep)" d="M178 0 H250 C230 200 330 430 520 602 H370 C220 470 150 240 178 0 Z"/>
    <path class="swoosh-light" fill="var(--purple)" d="M248 0 H282 C300 220 430 440 700 530 C800 560 900 560 958 555 V602 H620 C400 540 255 330 248 0 Z"/>
    <circle class="hero-disc" cx="742" cy="220" r="185" fill="var(--purple-deep)"/>
  </svg>

  <div class="brand">
    <span class="brand-dot"></span>
    <span class="brand-name">zorvella</span>
  </div>

  <p class="card-number">5157 5500 0000 0000</p>
  <span class="bin">5157</span>
  <span class="valid-label">VALID<br>THRU</span>
  <span class="valid-date">10/20</span>

  <div class="features">
    <div class="feature" aria-label="Allowance">
      <svg viewBox="0 0 40 40" fill="none" stroke="#fff" stroke-width="3" stroke-linejoin="round">
        <rect x="5" y="12" width="30" height="20" rx="2"/>
        <path d="M5 12 L20 24 L35 12"/>
      </svg>
    </div>
    <div class="feature" aria-label="Mobile app">
      <svg viewBox="0 0 40 40" fill="none" stroke="#fff" stroke-width="3">
        <rect x="12" y="4" width="16" height="32" rx="3"/>
        <circle cx="20" cy="31" r="1.5" fill="#fff"/>
      </svg>
    </div>
    <div class="feature" aria-label="Savings">
      <svg viewBox="0 0 40 40" fill="none" stroke="#fff" stroke-width="3">
        <circle cx="20" cy="20" r="13"/>
        <path d="M20 12 V28 M24 15 H18 a3 3 0 0 0 0 6 h4 a3 3 0 0 1 0 6 H15"/>
      </svg>
    </div>
    <div class="feature" aria-label="Wallet">
      <svg viewBox="0 0 40 40" fill="none" stroke="#fff" stroke-width="3" stroke-linejoin="round">
        <rect x="5" y="11" width="30" height="22" rx="3"/>
        <path d="M27 19 H35 V26 H27 Z"/>
      </svg>
    </div>
  </div>

  <div class="network-badge">
    <span class="hologram"></span>
    <span class="network-name">plexicard</span>
  </div>
</div>
</body>
</html>
```